Real Estate Email Signature

I need a professional looking real estate email signature with my picture, logo, and Name, Real Estate Broker/Realtor, and Top of Harbeck logo

```html
<!DOCTYPE html>
<html lang="en">
<head>
<meta charset="UTF-8">
<title>Sam Ridley – Email Signature</title>
<link rel="stylesheet" href="https://fonts.googleapis.com/css2?family=Exo+2:wght@600;700;800&family=Open+Sans:wght@600;700&display=swap">
<style>
  :root {
    --canvas: #ffffff;
    --band: #01527f;
    --gold: #f6a900;
    --white: #ffffff;
    --rule: #8fb3cb;
    --ring: #0b4a6e;
    --photo-top: #b9bcc0;
    --photo-bottom: #4d4440;
    --brand-ink: #1d4f78;
  }
  * { margin: 0; padding: 0; box-sizing: border-box; }
  html, body {
    width: 1200px;
    height: 564px;
    overflow: hidden;
    background: var(--canvas);
  }
  .signature {
    position: relative;
    width: 1200px;
    height: 564px;
  }
  .band {
    position: absolute;
    left: 300px;
    top: 176px;
    width: 776px;
    height: 236px;
    background: var(--band);
    border-radius: 0 118px 118px 0;
  }
  .portrait {
    position: absolute;
    left: 102px;
    top: 152px;
    width: 282px;
    height: 282px;
    border-radius: 50%;
    border: 6px solid var(--white);
    background: radial-gradient(circle at 50% 40%, #c89a80 0 22%, transparent 23%),
                linear-gradient(180deg, var(--photo-top) 0%, var(--photo-top) 55%, var(--photo-bottom) 100%);
    box-shadow: 0 0 0 1px rgba(0,0,0,0.05);
  }
  .identity {
    position: absolute;
    left: 428px;
    top: 200px;
    width: 360px;
  }
  .identity__name {
    font-family: "Exo 2", sans-serif;
    font-weight: 800;
    font-size: 50px;
    letter-spacing: 2px;
    line-height: 1;
    color: var(--gold);
  }
  .identity__title {
    margin-top: 12px;
    font-family: "Open Sans", sans-serif;
    font-weight: 700;
    font-size: 22px;
    color: var(--white);
  }
  .identity__rule {
    margin-top: 16px;
    width: 356px;
    height: 1px;
    background: var(--rule);
  }
  .award {
    margin-top: 30px;
    display: flex;
    align-items: center;
    gap: 12px;
  }
  .award__mark {
    width: 24px;
    height: 34px;
    display: block;
  }
  .award__label {
    font-family: "Open Sans", sans-serif;
    font-weight: 700;
    font-size: 22px;
    letter-spacing: 0.5px;
    color: var(--white);
  }
  .brand {
    position: absolute;
    left: 845px;
    top: 182px;
    width: 226px;
    height: 226px;
    border-radius: 50%;
    background: var(--white);
    border: 5px solid var(--ring);
    display: flex;
    flex-direction: column;
    align-items: center;
    justify-content: center;
    gap: 10px;
  }
  .brand__dot {
    width: 40px;
    height: 40px;
    border-radius: 50%;
    background: var(--brand-ink);
  }
  .brand__name {
    font-family: "Exo 2", sans-serif;
    font-weight: 700;
    font-size: 22px;
    letter-spacing: 1px;
    color: var(--brand-ink);
  }
</style>
</head>
<body>
  <main class="signature">
    <div class="band"></div>

    <div class="portrait" role="img" aria-label="Head-and-shoulders portrait photo of the broker"></div>

    <section class="identity">
      <h1 class="identity__name">SAM RIDLEY</h1>
      <p class="identity__title">Real Estate Broker/Realtor</p>
      <div class="identity__rule"></div>
      <div class="award">
        <svg class="award__mark" viewBox="0 0 24 34" aria-hidden="true">
          <rect x="0" y="0" width="24" height="34" rx="2" fill="var(--gold)"/>
        </svg>
        <span class="award__label">TOP OF HARBECK</span>
      </div>
    </section>

    <div class="brand">
      <span class="brand__dot"></span>
      <span class="brand__name">RIDLEY HOMES</span>
    </div>
  </main>
</body>
</html>
```